Animal Eye Clinic needs a Business card

We are a new veterinary ophthalmology practice (Silverbrook Pet Vision Care) and we need a business card designed. We only see animal eyes - we are not a regular veterinary clinic. We already have a logo. We are looking for a professional, good looking business card to hand out to our clients. We are looking for something simple but professional and contemporary. Our logo is likely the only picture/graphic that needs to be on the card.

Contact Information for Business Card

Marisol Quent, BSc, DVM, MSc, DipACVO
Veterinary Ophthalmologist

Phone: 555.419.3067
Email: silverbrookpetvisioncare@mailvero.com
Website: silverbrookpetvisioncare.com
Address: 1875 Tessock Rd
Marrow Bend, ON, K7X 8M3

Colors

Designer to choose colors to be used in the design.

Requirements
Must have
• Our logo (attached)

```html
<!DOCTYPE html>
<html lang="en">
<head>
<meta charset="utf-8">
<title>Silverbrook Pet Vision Care – Business Card</title>
<link href="https://fonts.googleapis.com/css2?family=Montserrat:wght@600;700&family=Roboto:wght@400;500&display=swap" rel="stylesheet">
<style>
  :root {
    --teal: #0a8d9a;
    --paper: #f7f8f8;
    --ink: #4a4d50;
    --rule: #6b6e70;
    --backdrop: #e9e7e4;
    --white: #ffffff;
  }
  * { box-sizing: border-box; margin: 0; padding: 0; }
  html, body {
    width: 1200px; height: 961px; overflow: hidden;
    background: var(--backdrop);
  }
  .canvas { position: relative; width: 1200px; height: 961px; }
  .card {
    position: absolute; left: 220px;
    width: 760px; height: 434px;
    box-shadow: 0 6px 18px rgba(0,0,0,.12);
    overflow: hidden;
  }
  .card--front { top: 36px; background: var(--teal); }
  .card--back  { top: 492px; background: var(--paper); }

  .brand {
    position: absolute; display: flex; align-items: center; gap: 16px;
    font-family: "Montserrat", sans-serif; font-weight: 700;
    letter-spacing: .4px; line-height: 1.1; white-space: nowrap;
  }
  .brand__dot { border-radius: 50%; flex: none; }

  .card--front .brand { left: 140px; top: 160px; color: var(--white); font-size: 28px; }
  .card--front .brand__dot { background: var(--white); width: 62px; height: 62px; }

  .card--back .brand { right: 46px; top: 72px; color: var(--teal); font-size: 24px; }
  .card--back .brand__dot { background: var(--teal); width: 52px; height: 52px; }

  .front-url {
    position: absolute; left: 0; right: 0; top: 310px; text-align: center;
    font-family: "Roboto", sans-serif; font-size: 15px; letter-spacing: 2.5px;
    color: var(--white);
  }

  .rule-top {
    position: absolute; left: 372px; right: 46px; top: 150px;
    height: 1.5px; background: var(--rule);
  }
  .accent-bar {
    position: absolute; left: 0; top: 272px; width: 26px; height: 40px;
    background: var(--teal);
  }
  .person { position: absolute; left: 70px; top: 180px; right: 46px; }
  .person__name {
    font-family: "Montserrat", sans-serif; font-weight: 700; font-size: 19px;
    color: var(--teal); display: flex; align-items: center; gap: 18px;
    white-space: nowrap;
  }
  .person__name::after {
    content: ""; flex: 1; height: 1.5px; background: var(--rule);
  }
  .person__title {
    font-family: "Roboto", sans-serif; font-size: 18px; color: var(--ink);
    margin-top: 4px;
  }
  .contact { list-style: none; margin-top: 18px; }
  .contact li {
    display: flex; align-items: center; gap: 10px;
    font-family: "Roboto", sans-serif; font-size: 17px; color: var(--ink);
    line-height: 25px; white-space: nowrap;
  }
  .contact svg { width: 15px; height: 15px; flex: none; fill: var(--teal); }
</style>
</head>
<body>
<main class="canvas">
  <section class="card card--front">
    <div class="brand"><span class="brand__dot"></span><span>Silverbrook Pet Vision Care</span></div>
    <p class="front-url">www.silverbrookpetvisioncare.com</p>
  </section>

  <section class="card card--back">
    <div class="brand"><span class="brand__dot"></span><span>Silverbrook Pet Vision Care</span></div>
    <div class="rule-top"></div>
    <div class="accent-bar"></div>
    <div class="person">
      <h1 class="person__name">Marisol Quent, BSc, DVM, MSc, DipACVO</h1>
      <p class="person__title">Veterinary Ophthalmologist</p>
      <ul class="contact">
        <li><svg viewBox="0 0 24 24" aria-hidden="true"><path d="M6.6 10.8a15 15 0 0 0 6.6 6.6l2.2-2.2a1 1 0 0 1 1-.25 11.4 11.4 0 0 0 3.6.57 1 1 0 0 1 1 1V20a1 1 0 0 1-1 1A17 17 0 0 1 3 4a1 1 0 0 1 1-1h3.5a1 1 0 0 1 1 1c0 1.25.2 2.45.57 3.57a1 1 0 0 1-.25 1z"/></svg>555.419.3067</li>
        <li><svg viewBox="0 0 24 24" aria-hidden="true"><path d="M2 5h20v14H2z M3.5 6.5 12 13l8.5-6.5" fill="none" stroke="#0a8d9a" stroke-width="2"/></svg>silverbrookpetvisioncare@mailvero.com</li>
        <li><svg viewBox="0 0 24 24" aria-hidden="true"><circle cx="12" cy="12" r="9" fill="none" stroke="#0a8d9a" stroke-width="2"/><path d="M3 12h18M12 3c3 3 3 15 0 18M12 3c-3 3-3 15 0 18" fill="none" stroke="#0a8d9a" stroke-width="1.6"/></svg>www.silverbrookpetvisioncare.com</li>
        <li><svg viewBox="0 0 24 24" aria-hidden="true"><path d="M12 2a7 7 0 0 0-7 7c0 5 7 13 7 13s7-8 7-13a7 7 0 0 0-7-7zm0 9.5A2.5 2.5 0 1 1 12 6.5a2.5 2.5 0 0 1 0 5z"/></svg>1875 Tessock Rd Marrow Bend, ON, K7X 8M3</li>
      </ul>
    </div>
  </section>
</main>
</body>
</html>
```